bright-vale.net Real Estate, Investment, Financial corporate

Real Estate, Investment, Financial corporate looking site. Show present a professional firm, with an elegant display. Please see the attached file which includes the logo, palette and fonts.
Updates

We just starting the brief today. ( logo was delayed)

Target Market(s)

Investors, Corporate , B2b

Industry/Entity Type

real-estate investments

Number of Pages Required

3 page

Requirements
Must have
• Dazzling Homepage
Nice to have
• paralex

```html
<!DOCTYPE html>
<html lang="en">
<head>
<meta charset="utf-8">
<title>Veldan — Real Estate, Investment, Financial Corporate</title>
<link rel="stylesheet" href="https://fonts.googleapis.com/css2?family=Poppins:wght@300;400;500;600;700;800&family=Roboto:wght@400;500&display=swap">
<style>
:root{
  --green:#5e9d3f;
  --green-band:#6aa84a;
  --dark:#3b4045;
  --nav:#3d4246;
  --footer:#2b2f31;
  --text:#555b60;
  --muted:#6d7276;
  --light:#f4f4f4;
  --white:#ffffff;
}
*{margin:0;padding:0;box-sizing:border-box}
html,body{width:1200px;height:2828px;overflow:hidden}
body{position:relative;background:var(--white);font-family:'Poppins',sans-serif;color:var(--dark)}
.abs{position:absolute}

/* header */
.site-header{position:absolute;left:0;top:0;width:1200px;height:68px;background:var(--white)}
.social{position:absolute;display:flex;gap:7px}
.social span{display:block;width:34px;height:34px;border-radius:50%;border:1.5px solid var(--dark)}
.social span:first-child{border-color:var(--green)}
.header-social{left:60px;top:17px}
.brand{position:absolute;left:0;width:1200px;text-align:center;font-weight:700;letter-spacing:-1px}
.header-brand{top:14px;font-size:32px;color:#4a4f54}
.call{position:absolute;left:953px;top:14px;display:flex;align-items:center;gap:8px}
.call-icon{width:40px;height:40px;border-radius:50%;border:2px solid var(--green);display:flex;align-items:center;justify-content:center}
.call small{display:block;font-size:12px;color:var(--green);line-height:14px}
.call strong{display:block;font-size:17px;font-weight:600;color:var(--dark);line-height:22px}

/* nav */
.main-nav{position:absolute;left:0;top:68px;width:1200px;height:44px;background:var(--nav);display:flex;justify-content:center}
.main-nav a{display:block;height:44px;line-height:44px;padding:0 23px;font-size:11.5px;color:#e8e8e8;text-decoration:none;border-right:1px solid #4b5055}
.main-nav a:last-child{border-right:0}
.main-nav a.active{background:var(--green);color:#fff;padding:0 18px;border-right:0}

/* hero */
.hero{position:absolute;left:0;top:112px;width:1200px;height:600px;background:linear-gradient(180deg,#6e7176 0%,#7d8084 45%,#9a9a98 75%,#b7b3ad 100%)}
.hero-kicker{position:absolute;left:0;top:197px;width:1200px;text-align:center;color:#fff;font-size:16px;letter-spacing:9px;font-weight:400}
.hero-title{position:absolute;left:0;top:222px;width:1200px;text-align:center;color:#fff;font-size:72px;font-weight:800;letter-spacing:-1px;line-height:90px}
.hero-tags{position:absolute;left:390px;top:316px;width:420px;height:34px;background:var(--green);color:#fff;font-family:'Roboto',sans-serif;font-size:16.5px;text-align:center;line-height:34px}

/* service cards */
.card{position:absolute;top:712px;height:270px;background:#fff;box-shadow:0 3px 12px rgba(0,0,0,.07);text-align:center}
.card-icon{position:absolute;top:-44px;left:50%;margin-left:-45px;width:90px;height:90px;background:var(--green);display:flex;align-items:center;justify-content:center}
.card h3{position:absolute;top:80px;left:0;width:100%;font-size:19px;font-weight:600;color:var(--dark)}
.card p{position:absolute;top:116px;left:26px;right:26px;font-size:11.5px;line-height:19px;color:var(--muted);font-weight:300}

/* about */
.about-photo{position:absolute;left:0;top:1061px;width:585px;height:458px;background:linear-gradient(135deg,#b9c3cb 0%,#8d98a2 40%,#47505a 65%,#c8cdd2 100%)}
.about{position:absolute;left:585px;top:1061px;width:615px;height:458px;background:var(--light)}
.about .hello{position:absolute;left:92px;top:74px;font-size:14px;color:var(--dark)}
.about h2{position:absolute;left:91px;top:98px;font-size:33px;line-height:38px;font-weight:700;color:var(--dark)}
.about h2 em{font-style:normal;color:var(--green);display:block}
.about .lead{position:absolute;left:92px;top:188px;width:360px;font-size:14.5px;line-height:23px;color:var(--dark)}
.about .body{position:absolute;left:92px;top:246px;width:385px;font-size:11.5px;line-height:21px;color:var(--muted);font-weight:300}
.btn{position:absolute;left:94px;top:346px;width:143px;height:41px;background:var(--green);color:#fff;font-size:15px;font-weight:600;text-align:center;line-height:41px}

/* portfolio */
.section-title{position:absolute;left:0;top:1585px;width:1200px;text-align:center;font-size:35px;font-weight:700;color:var(--dark)}
.section-title em{font-style:normal;color:var(--green)}
.section-sub{position:absolute;left:0;top:1639px;width:1200px;text-align:center;font-size:12.5px;line-height:21px;color:var(--dark)}
.tile{position:absolute;width:285px;height:210px}
.explore{position:absolute;left:0;top:2205px;width:1200px;text-align:center;font-size:15px;font-weight:600;font-style:italic;color:var(--green);text-decoration:underline}

/* call to action */
.cta{position:absolute;left:0;top:2364px;width:1200px;height:187px;background:var(--green-band)}
.cta h2{position:absolute;left:181px;top:40px;font-size:21.5px;line-height:30px;font-weight:700;color:var(--dark)}
.cta-phone{position:absolute;left:181px;top:112px;display:flex;align-items:center;gap:10px;color:#fff;font-size:20px;font-weight:600}
.cta-phone .ring{width:38px;height:38px;border-radius:50%;border:2px solid #fff;display:flex;align-items:center;justify-content:center}
.cta-person{position:absolute;left:770px;top:2248px;width:235px;height:303px;background:linear-gradient(180deg,#d9c7b6 0%,#8a4b4b 40%,#5a3a48 100%);border-radius:110px 110px 0 0}

/* footer */
.site-footer{position:absolute;left:0;top:2551px;width:1200px;height:277px;background:var(--footer)}
.footer-brand{top:64px;font-size:32px;color:#4c5156}
.footer-social{left:521px;top:118px}
.footer-social span{border-color:#55595d}
.footer-social span:first-child{background:var(--green);border-color:var(--green)}
.footer-links{position:absolute;left:0;top:174px;width:1200px;text-align:center;font-size:12px;color:#b9bcbe}
.footer-links a{color:#b9bcbe;text-decoration:none;padding:0 9px}
.footer-links a:first-child{color:var(--green)}
.copyright{position:absolute;left:0;top:198px;width:1200px;text-align:center;font-size:12px;color:#d0d2d3}
.copyright span{color:var(--green)}
</style>
</head>
<body>

<header class="site-header">
  <div class="social header-social"><span></span><span></span><span></span><span></span></div>
  <div class="brand header-brand">Veldan</div>
  <div class="call">
    <div class="call-icon">
      <svg width="20" height="20" viewBox="0 0 24 24"><path d="M6.6 10.8c1.4 2.8 3.8 5.1 6.6 6.6l2.2-2.2c.3-.3.7-.4 1-.2 1.1.4 2.3.6 3.6.6.6 0 1 .4 1 1V20c0 .6-.4 1-1 1C10.6 21 3 13.4 3 4c0-.6.4-1 1-1h3.5c.6 0 1 .4 1 1 0 1.3.2 2.5.6 3.6.1.3 0 .7-.2 1z" fill="none" stroke="#5e9d3f" stroke-width="1.6"/></svg>
    </div>
    <div><small>Call Us Today</small><strong>(+1) 555 014 2290</strong></div>
  </div>
</header>

<nav class="main-nav">
  <a class="active">HOME</a><a>ABOUT US</a><a>SERVICES</a><a>PORTFOLIO</a><a>NEWS</a><a>CONTACT US</a>
</nav>

<section class="hero" role="img" aria-label="Three business people around a table with wooden house models in a bright office">
  <div class="hero-kicker">REAL ESTATE IS</div>
  <h1 class="hero-title">OUR PASSION</h1>
  <div class="hero-tags">Real Estate &nbsp;|&nbsp; Investment &nbsp;|&nbsp; Financial Corporate</div>
</section>

<article class="card" style="left:175px;width:256px">
  <div class="card-icon">
    <svg width="60" height="60" viewBox="0 0 60 60" fill="none" stroke="#fff" stroke-width="2"><path d="M6 28 26 8l20 20M12 22v26h22M22 48V34h8v8"/><circle cx="44" cy="44" r="9"/><path d="m40 44 3 3 6-6"/></svg>
  </div>
  <h3>Real Estate</h3>
  <p>Lorem Ipsum is simply dummy text of the printing and typesetting industry. Lorem Ipsum has been the industry's standard dummy text ever since the 1500s, when an unknown..</p>
</article>

<article class="card" style="left:468px;width:264px">
  <div class="card-icon">
    <svg width="60" height="60" viewBox="0 0 60 60" fill="none" stroke="#fff" stroke-width="2"><path d="M8 6v46h46"/><path d="M16 50V38h6v12M26 50V32h6v18M36 50V26h6v24M46 50V18h6v32"/><path d="M14 32 26 22l8 6 16-16M44 12h6v6"/></svg>
  </div>
  <h3>Investment</h3>
  <p>Lorem Ipsum is simply dummy text of the printing and typesetting industry. Lorem Ipsum has been the industry's standard dummy text ever since the 1500s, when an unknown..</p>
</article>

<article class="card" style="left:770px;width:255px">
  <div class="card-icon">
    <svg width="60" height="60" viewBox="0 0 60 60" fill="none" stroke="#fff" stroke-width="2"><path d="M30 8h8l-4 6M26 14h14M28 14c-8 6-12 14-10 20 2 5 8 6 14 6s12-1 14-6c2-6-2-14-10-20"/><path d="M36 22c-3-1-6 0-6 2s6 2 6 5-4 3-7 2M33 19v3M33 31v3"/><path d="M4 46l10-6c4-2 8-1 12 1h10c2 0 2 4 0 4H24M36 45l12-5c3-1 5 2 2 4L36 52H20L8 54"/></svg>
  </div>
  <h3>Financial Corporate</h3>
  <p>Lorem Ipsum is simply dummy text of the printing and typesetting industry. Lorem Ipsum has been the industry's standard dummy text ever since the 1500s, when an unknown..</p>
</article>

<div class="about-photo" role="img" aria-label="Businessman pointing a pen at a dark architectural building model on a desk"></div>
<section class="about">
  <div class="hello">Welcome To</div>
  <h2>VELDAN<em>BRIGHT VALE</em></h2>
  <p class="lead">Lorem Ipsum is simply dummy text of the printing and typesetting industry Lorem Ipsum been.</p>
  <p class="body">Lorem Ipsum is simply dummy text of the printing and typesetting industry. Lorem Ipsum has been the industry's standard dummy text ever since the 1500s, when an unknown printer took a galley of type and scrambled it to specimen book.</p>
  <div class="btn">LEARN MORE</div>
</section>

<h2 class="section-title">WORK <em>PORTFOLIO</em></h2>
<p class="section-sub">Lorem Ipsum is simply dummy text of the printing and typesetting<br>industry Lorem Ipsum been.</p>

<div class="tile" style="left:150px;top:1711px;background:linear-gradient(180deg,#6fa24a,#79b04f)" role="img" aria-label="Suburban house with lawn under a green overlay"></div>
<div class="tile" style="left:457px;top:1733px;background:linear-gradient(180deg,#6c7480,#4a5560 60%,#3c4650)" role="img" aria-label="Modern grey house at dusk with lit entrance"></div>
<div class="tile" style="left:765px;top:1711px;background:linear-gradient(180deg,#d8dde2,#cfcac0 50%,#4f7a33)" role="img" aria-label="White modern villa with trimmed hedges"></div>
<div class="tile" style="left:150px;top:1943px;background:linear-gradient(180deg,#c7d4e2,#6a5e52 55%,#2f2a26)" role="img" aria-label="Stone and wood house lit at night"></div>
<div class="tile" style="left:457px;top:1966px;background:linear-gradient(180deg,#2e4054,#8a8c8e 55%,#555a5f)" role="img" aria-label="Row of townhouses on a street at dusk"></div>
<div class="tile" style="left:765px;top:1943px;background:linear-gradient(180deg,#6f8aa6,#3d5068 50%,#8a5a3c 80%,#2f7fb0)" role="img" aria-label="Modern villa with pool at night"></div>

<div class="explore">Explore All</div>

<section class="cta">
  <h2>NEED AN HAVE ANY QUESTION OR<br>REAL ESTATE SERVICES HELP ?</h2>
  <div class="cta-phone">
    <span class="ring"><svg width="20" height="20" viewBox="0 0 24 24"><path d="M6.6 10.8c1.4 2.8 3.8 5.1 6.6 6.6l2.2-2.2c.3-.3.7-.4 1-.2 1.1.4 2.3.6 3.6.6.6 0 1 .4 1 1V20c0 .6-.4 1-1 1C10.6 21 3 13.4 3 4c0-.6.4-1 1-1h3.5c.6 0 1 .4 1 1 0 1.3.2 2.5.6 3.6.1.3 0 .7-.2 1z" fill="none" stroke="#fff" stroke-width="1.6"/></svg></span>
    (+1) 555 014 2290
  </div>
</section>
<div class="cta-person" role="img" aria-label="Smiling man in a plaid shirt holding a tablet"></div>

<footer class="site-footer">
  <div class="brand footer-brand">Veldan</div>
  <div class="social footer-social"><span></span><span></span><span></span><span></span></div>
  <div class="footer-links"><a>Home</a>|<a>About</a>|<a>Services</a>|<a>Portfolio</a>|<a>News</a>|<a>Contact Us</a></div>
  <div class="copyright">©<span>Veldan Bright Vale</span> - 2021 All rights reserved.</div>
</footer>

</body>
</html>
```